Residential Construction Business - Site Signage

I need a design made for a site fence banner. We have a logo and branding so the design would need to be aligned with this. It would need to be made to specific size ratio so that it can be sent to the maker for production.
ratio : 4600 wide x 1700 high
The design should feature our website and also the slogan
"don't move, re-imagine"

Target Market(s)

potential clients

Industry/Entity Type

construction

Font styles to use
Other font styles liked:
• to match branding

Colors
0054AA
0677BA
7BADD7
CADEEF
E8F1F8

Requirements
Must have
• www.velmbuild.com.au Majority of the sign is our brand logo
Nice to have
• Majority of the sign is our brand logo
Should not have
• colors and themes that arent brand relevant

```html
<!DOCTYPE html>
<html lang="en">
<head>
<meta charset="utf-8">
<title>Velm Build – Site Fence Banner Options</title>
<link href="https://fonts.googleapis.com/css2?family=Montserrat:wght@500;600&display=swap" rel="stylesheet">
<style>
  :root {
    --navy: #043b5f;
    --paper: #ffffff;
    --backdrop: #e1e1e1;
  }
  * { margin: 0; padding: 0; box-sizing: border-box; }
  html, body {
    width: 1200px; height: 1200px; overflow: hidden;
    background: var(--backdrop);
    font-family: "Montserrat", Arial, sans-serif;
  }
  .banner {
    position: absolute;
    left: 211px;
    width: 778px;
    height: 281px;
    background: var(--paper);
    overflow: hidden;
  }
  .banner--one { top: 127px; }
  .banner--two { top: 460px; }
  .banner--three { top: 792px; }
  .banner__field { position: absolute; inset: 0; width: 100%; height: 100%; }
  .banner__field path { fill: var(--navy); }

  .brand-name {
    position: absolute;
    font-weight: 600;
    font-size: 23px;
    letter-spacing: 0.36em;
    line-height: 1;
    color: var(--navy);
    white-space: nowrap;
    transform: translateY(-50%);
  }

  .slogan {
    position: absolute;
    font-weight: 600;
    line-height: 1;
    white-space: nowrap;
  }
  .slogan__line { position: absolute; font-size: 43px; }
  .slogan__rule { position: absolute; height: 2px; }

  .website {
    position: absolute;
    font-weight: 500;
    font-size: 14px;
    letter-spacing: 0.06em;
    line-height: 1;
    white-space: nowrap;
  }

  /* Option one: slogan on navy, centred */
  .banner--one .slogan { color: var(--paper); }
  .banner--one .slogan__line { left: 199px; transform: translateX(-50%); }
  .banner--one .slogan__line--top { top: 80px; }
  .banner--one .slogan__line--bottom { top: 151px; }
  .banner--one .slogan__rule { left: 66px; width: 265px; top: 134px; background: var(--paper); }
  .banner--one .brand-name { left: 512px; top: 141px; }
  .banner--one .website { left: 199px; top: 222px; transform: translateX(-50%); color: var(--paper); }

  /* Option two: slogan on white, left aligned */
  .banner--two .slogan { color: var(--navy); }
  .banner--two .slogan__line { left: 463px; }
  .banner--two .slogan__line--top { top: 80px; }
  .banner--two .slogan__line--bottom { top: 150px; }
  .banner--two .slogan__rule { left: 464px; width: 265px; top: 132px; background: var(--navy); }
  .banner--two .brand-name { left: 214px; top: 140px; }
  .banner--two .website { left: 465px; top: 222px; color: var(--navy); }

  /* Option three: compact slogan, bottom right */
  .banner--three .slogan--compact {
    position: absolute;
    right: 43px;
    top: 160px;
    text-align: right;
    color: var(--navy);
    font-size: 31px;
    line-height: 38px;
  }
  .banner--three .brand-name { left: 214px; top: 87px; }
  .banner--three .website { right: 45px; top: 243px; color: var(--navy); }
</style>
</head>
<body>

  <section class="banner banner--one">
    <svg class="banner__field" viewBox="0 0 778 281" preserveAspectRatio="none" aria-hidden="true">
      <path d="M0 0 H622 L496 127 Q489 140.5 496 154 L622 281 H0 Z"/>
    </svg>
    <div class="slogan">
      <span class="slogan__line slogan__line--top">don’t move,</span>
      <span class="slogan__rule"></span>
      <span class="slogan__line slogan__line--bottom">re-imagine</span>
    </div>
    <span class="website">www.velmbuild.com.au</span>
    <span class="brand-name">VELM BUILD</span>
  </section>

  <section class="banner banner--two">
    <svg class="banner__field" viewBox="0 0 778 281" preserveAspectRatio="none" aria-hidden="true">
      <path d="M0 0 H324 L198 127 Q191 140.5 198 154 L324 281 H0 Z"/>
    </svg>
    <span class="brand-name">VELM BUILD</span>
    <div class="slogan">
      <span class="slogan__line slogan__line--top">don’t move,</span>
      <span class="slogan__rule"></span>
      <span class="slogan__line slogan__line--bottom">re-imagine</span>
    </div>
    <span class="website">www.velmbuild.com.au</span>
  </section>

  <section class="banner banner--three">
    <svg class="banner__field" viewBox="0 0 778 281" preserveAspectRatio="none" aria-hidden="true">
      <path d="M0 0 H271 L197 75 Q189 87 197 99 L378 281 H0 Z"/>
    </svg>
    <span class="brand-name">VELM BUILD</span>
    <p class="slogan slogan--compact">don’t move,<br>re-imagine</p>
    <span class="website">www.velmbuild.com.au</span>
  </section>

</body>
</html>
```